Postcard Design

Company Name--motion harbor
482 Garnet Avenue
Brooklyn New York11231
347-555-0182
www.motionharbors. example
We are a boutique personal fitness company in a exclusive neighnorhood in Brooklyn New York. We specialize in personal training and innovate new fitness classes such as Pulse-Circuit QVR and Tabata.

We want our brand to be high-end but open to all. Laid-back but experts in the field of fitness. Innovative and flexible. Proffessional, friendly and inspiring.

Personal attention for our clients is a must as well as making sure they succeed. 87% of our clients reach their goals.

Colors should be bright but sophisticated with a little aggression but not intimidation.
Updates

Company Name-And contact info has been updated on the brief

I posted a logo. And the colors on the website have changed. If you could incorporate the website color scheme that would be helpful. If for whatever reason the logo is not here I will try to upload again.

Change the contact info: www.motionharbors.example You tube: Brisco and the Motion Harbor Email: Motionharbors@mailbox.example Verbiage changes: 'The only boutique personal fitness studio in Brooklyn. Featuring uniquely proprietary classes QVR, Cross Training and now Tabata." Verbiage Additions Safe for moms, dads and we offer enhanced childcare with certified child care development teachers with our partner studios. Classes start at $15

Please Add : Use this postcard to receive 10% any service

Hi, I could not upload the logo. However they said that our Logo should be uploaded now as I sent it to them manually.

Target Market(s)

30-40 year old women and new moms looking to do cross fit and personal training. Income 80-85K.

Industry/Entity Type

Boutique

Requirements
Must have
• Highlight Tabata and the excellence of the classes.Tag lines- Increase calorie burn by 20%. Increase muscle tone by 25%.Increase metabolism by 25%. Classes only available by appointment. 30mins or 1 hour.
Nice to have
• Attractive and fit young people having fun. Personal training.
Should not have
• Overly sexual fitness models.

```html
<!DOCTYPE html>
<html lang="en">
<head>
<meta charset="utf-8">
<title>Motion Harbor Postcard</title>
<link rel="stylesheet" href="https://fonts.googleapis.com/css2?family=Barlow+Condensed:ital,wght@0,400;0,600;0,700;1,700&display=swap">
<style>
  :root {
    --canvas: #ffffff;
    --board: #1e1e1e;
    --board-light: #2e2e2e;
    --magenta: #e8008a;
    --magenta-deep: #b8125a;
    --hazard: #e9e21a;
    --ink-dark: #2a2a2a;
    --white: #ffffff;
  }
  html, body {
    margin: 0;
    padding: 0;
    width: 1200px;
    height: 924px;
    overflow: hidden;
    background: var(--canvas);
  }
  .postcard {
    position: absolute;
    left: 0;
    top: 0;
    width: 580px;
    height: 763px;
    overflow: hidden;
    font-family: "Barlow Condensed", "Arial Narrow", sans-serif;
    color: var(--white);
  }
  .postcard__backdrop {
    position: absolute;
    inset: 0;
    background: linear-gradient(100deg, var(--board) 0%, var(--board-light) 45%, var(--board) 100%);
  }
  .postcard__shapes {
    position: absolute;
    inset: 0;
  }
  .brand-name {
    position: absolute;
    left: 42px;
    top: 44px;
    margin: 0;
    font-weight: 700;
    font-size: 70px;
    line-height: 1;
    letter-spacing: -1px;
    color: var(--white);
  }
  .headline {
    position: absolute;
    left: 0;
    width: 580px;
    margin: 0;
    text-align: center;
    font-style: italic;
    font-weight: 700;
    letter-spacing: -0.5px;
  }
  .headline--intro {
    top: 210px;
    font-size: 44px;
    line-height: 43px;
    padding-right: 10px;
    box-sizing: border-box;
  }
  .headline--classes {
    top: 322px;
    font-size: 46px;
    line-height: 44px;
  }
  .class-name { color: var(--magenta); }
  .details {
    position: absolute;
    left: 0;
    top: 481px;
    width: 574px;
    margin: 0;
    text-align: center;
    font-weight: 700;
    font-size: 29px;
    line-height: 33px;
    letter-spacing: -0.4px;
  }
  .price {
    position: absolute;
    left: 0;
    top: 594px;
    width: 574px;
    margin: 0;
    text-align: center;
    font-weight: 700;
    font-size: 29px;
    line-height: 1;
    color: var(--magenta);
  }
  .video-callout {
    position: absolute;
    left: 122px;
    top: 690px;
    margin: 0;
    color: var(--ink-dark);
  }
  .video-callout__lead {
    display: block;
    font-weight: 400;
    font-size: 20px;
    line-height: 22px;
    letter-spacing: 0.3px;
  }
  .video-callout__channel {
    display: block;
    font-weight: 700;
    font-size: 27px;
    line-height: 30px;
  }
</style>
</head>
<body>
  <article class="postcard">
    <div class="postcard__backdrop" role="img" aria-label="Dark weathered wood plank texture"></div>

    <svg class="postcard__shapes" width="580" height="763" viewBox="0 0 580 763" aria-hidden="true">
      <defs>
        <pattern id="hazard-stripes" width="10" height="10" patternUnits="userSpaceOnUse" patternTransform="rotate(45)">
          <rect width="10" height="10" fill="#111"/>
          <rect width="5" height="10" fill="var(--hazard)"/>
        </pattern>
        <pattern id="light-stripes" width="10" height="10" patternUnits="userSpaceOnUse" patternTransform="rotate(45)">
          <rect width="10" height="10" fill="#111"/>
          <rect width="5" height="10" fill="#ffffff"/>
        </pattern>
        <linearGradient id="banner-fill" x1="0" x2="1" y1="0" y2="0">
          <stop offset="0" stop-color="var(--magenta-deep)"/>
          <stop offset="0.35" stop-color="var(--magenta)"/>
          <stop offset="1" stop-color="var(--magenta)"/>
        </linearGradient>
        <linearGradient id="footer-fill" x1="0" x2="1" y1="0" y2="0">
          <stop offset="0" stop-color="var(--magenta)"/>
          <stop offset="0.7" stop-color="var(--magenta)"/>
          <stop offset="1" stop-color="var(--magenta-deep)"/>
        </linearGradient>
      </defs>

      <polygon class="band-hazard-top" points="0,0 510,0 484,30 0,30" fill="url(#hazard-stripes)"/>
      <polygon class="banner-brand" points="0,32 533,32 430,148 0,148" fill="url(#banner-fill)"/>
      <polygon class="band-stripes-light" points="0,150 372,150 358,166 0,166" fill="url(#light-stripes)"/>

      <polygon class="band-hazard-bottom" points="144,663 580,663 580,678 130,678" fill="url(#hazard-stripes)"/>
      <polygon class="banner-footer" points="0,763 85,679 580,679 580,763" fill="url(#footer-fill)"/>
      <rect class="channel-mark" x="473" y="695" width="46" height="46" rx="5" fill="#111" stroke="#ddd" stroke-width="1"/>
    </svg>

    <h1 class="brand-name">Motion Harbor</h1>

    <p class="headline headline--intro">The only boutique personal<br>fitness studio in Brooklyn!</p>

    <p class="headline headline--classes">Featuring uniquely proprietary<br>classes <span class="class-name">QVR</span>, <span class="class-name">Cross Trainning</span><br>and now <span class="class-name">Tabata</span>.</p>

    <p class="details">Safe for moms and dads. We offer enhanced<br>childcare with certified child care development<br>teachers with our partner studios.</p>

    <p class="price">CLASSES START AT $15</p>

    <p class="video-callout">
      <span class="video-callout__lead">Check out our ClipCast videos at:</span>
      <span class="video-callout__channel">Brisco and the Motion Harbor</span>
    </p>
  </article>
</body>
</html>
```